Upscale business cards needed for family business

We need professional business cards created for several family members. We are a family business holding company. We would like these relatively simple and straightforward, but also with a unique element to set them apart. Probably stick with neutral and simple colors - white, grey etc. We need space for the traditional elements, including name, title, address, email/phone number. And we will be creating several from this template so it needs to be template that is easy to switch information in and out of.

Industry/Entity Type

Business

Contact Information for Business Card

Please include the attached Dunmore Ventures logo.

Requirements
Must have
• The attached Dunmore Ventures logo.

```html
<!DOCTYPE html>
<html lang="en">
<head>
<meta charset="utf-8">
<title>Dunmore Ventures Business Card</title>
<link href="https://fonts.googleapis.com/css2?family=Cinzel:wght@400;600&family=Open+Sans:wght@400;600&family=Tinos&display=swap" rel="stylesheet">
<style>
  :root {
    --backdrop: #3d3d3d;
    --card-white: #ffffff;
    --gold: #c9992a;
    --gold-light: #ebc32f;
    --gold-deep: #c99a38;
    --ink: #222222;
    --ink-soft: #4a4a4a;
    --logo-ink: #3a3a3a;
  }
  * { margin: 0; padding: 0; box-sizing: border-box; }
  html, body {
    width: 1105px;
    height: 1200px;
    overflow: hidden;
    background: var(--backdrop);
  }
  .sheet {
    position: relative;
    width: 1105px;
    height: 1200px;
  }
  .card {
    position: absolute;
    left: 196px;
    width: 720px;
    height: 412px;
    box-shadow: 0 3px 8px rgba(0,0,0,0.45);
  }
  .card--front { top: 146px; background: var(--card-white); }
  .card--back {
    top: 602px;
    background: radial-gradient(ellipse at 50% 38%, var(--gold-light) 0%, #ddb132 45%, var(--gold-deep) 100%);
  }
  .brand {
    position: absolute;
    font-family: "Cinzel", serif;
    font-weight: 400;
    text-align: center;
    line-height: 1.15;
  }
  .card--front .brand {
    right: 40px;
    top: 78px;
    width: 310px;
    font-size: 27px;
    color: var(--logo-ink);
  }
  .card--back .brand {
    left: 0;
    right: 0;
    top: 195px;
    font-size: 37px;
    color: #ffffff;
  }
  .holder {
    position: absolute;
    left: 47px;
    top: 180px;
  }
  .holder__name {
    font-family: "Cinzel", serif;
    font-weight: 600;
    font-size: 30px;
    color: var(--gold);
    letter-spacing: 0.5px;
    line-height: 1.1;
  }
  .holder__title {
    font-family: "Open Sans", sans-serif;
    font-size: 19px;
    color: var(--ink);
    margin-top: 2px;
  }
  .contacts {
    position: absolute;
    left: 47px;
    top: 258px;
    list-style: none;
  }
  .contacts__item {
    display: flex;
    align-items: center;
    height: 29px;
    font-family: "Tinos", serif;
    font-size: 20px;
    color: var(--ink-soft);
  }
  .contacts__item:last-child { margin-top: 3px; }
  .contacts__icon {
    width: 18px;
    height: 18px;
    margin-right: 9px;
    fill: var(--gold);
    flex: none;
  }
  .web {
    position: absolute;
    left: 0;
    right: 0;
    top: 336px;
    text-align: center;
    font-family: "Open Sans", sans-serif;
    font-size: 19px;
    letter-spacing: 1px;
    color: #ffffff;
  }
</style>
</head>
<body>
<main class="sheet">
  <section class="card card--front">
    <div class="brand">Dunmore Ventures Inc</div>
    <div class="holder">
      <h1 class="holder__name">Owen Marlow</h1>
      <p class="holder__title">CEO/Founder</p>
    </div>
    <ul class="contacts">
      <li class="contacts__item">
        <svg class="contacts__icon" viewBox="0 0 24 24" aria-hidden="true"><path d="M6.6 10.8a15 15 0 0 0 6.6 6.6l2.2-2.2c.3-.3.7-.4 1-.2 1.1.4 2.3.6 3.6.6.6 0 1 .4 1 1V20c0 .6-.4 1-1 1A17 17 0 0 1 3 4c0-.6.4-1 1-1h3.5c.6 0 1 .4 1 1 0 1.3.2 2.5.6 3.6.1.3 0 .7-.2 1z"/></svg>
        512 608 4190
      </li>
      <li class="contacts__item">
        <svg class="contacts__icon" viewBox="0 0 24 24" aria-hidden="true"><path d="M3 6h18v12H3z M3 6l9 7 9-7" stroke="#fff" stroke-width="1.5"/></svg>
        owen@dunmoreventures.com
      </li>
      <li class="contacts__item">
        <svg class="contacts__icon" viewBox="0 0 24 24" aria-hidden="true"><circle cx="12" cy="12" r="10"/><path d="M2 12h20M12 2c3 3 3 17 0 20M12 2c-3 3-3 17 0 20" stroke="#fff" stroke-width="1.3" fill="none"/></svg>
        www.dunmoreventures.com
      </li>
      <li class="contacts__item">
        <svg class="contacts__icon" viewBox="0 0 24 24" aria-hidden="true"><path d="M12 2a7 7 0 0 0-7 7c0 5 7 13 7 13s7-8 7-13a7 7 0 0 0-7-7zm0 9.5A2.5 2.5 0 1 1 12 6.5a2.5 2.5 0 0 1 0 5z"/></svg>
        214 Cedar Ridge Road, Fairbanks, Alaska 99701
      </li>
    </ul>
  </section>

  <section class="card card--back">
    <div class="brand">Dunmore Ventures Inc</div>
    <p class="web">www.dunmoreventuresinc.com</p>
  </section>
</main>
</body>
</html>
```